Business Card and Letterhead for Nurlo - modern real estate business

I need a double sided business card design for Nurlo. Please see business card brief here https://papers.trelvimo.net/sheet/q/7XrTbaLeZpMmQ2uWvd9HkCj4yNoEfsGi3lRtAz_pk/view?mode=shared

Please feel free to design the business cards however you feel best. I am happy to give some creative freedoms and then provide feedback from there.

Please then also create a letterhead to match the business card design

Colors

Designer to choose colors to be used in the design.

Requirements
Must have
• Must be a modern, elegant business card which looks very professional

```html
<!DOCTYPE html>
<html lang="en">
<head>
<meta charset="utf-8">
<title>Nurlo – Business Card</title>
<link rel="stylesheet" href="https://fonts.googleapis.com/css2?family=Montserrat:wght@400;500;600;700&display=swap">
<style>
  :root {
    --canvas: #2e2824;
    --card: #333335;
    --card-back: #2c2d30;
    --edge: #e0141c;
    --accent: #e8141c;
    --text: #ffffff;
    --muted: #c9c9cc;
    --emboss: #3c3d41;
    --photo-top: #4a4a4e;
    --photo-bottom: #26262a;
  }
  * { box-sizing: border-box; margin: 0; padding: 0; }
  html, body {
    width: 1200px; height: 800px; overflow: hidden;
    background: var(--canvas);
    font-family: "Montserrat", sans-serif;
  }
  .stage { position: relative; width: 1200px; height: 800px; }
  .card {
    position: absolute; top: 245px;
    width: 540px; height: 310px;
    border: 2px solid var(--edge);
    overflow: hidden;
  }
  .card--back { left: 40px; background: var(--card-back); }
  .card--front { left: 620px; background: var(--card); }

  .back-mark {
    position: absolute; inset: 0;
    display: flex; align-items: center; justify-content: center;
    font-weight: 700; font-size: 78px; letter-spacing: 6px;
    color: var(--emboss);
  }

  .portrait {
    position: absolute; left: 0; bottom: 0;
    width: 240px; height: 270px;
    background: linear-gradient(180deg, var(--photo-top), var(--photo-bottom));
    border-radius: 110px 110px 0 0;
  }

  .details {
    position: absolute; right: 28px; top: 34px;
    width: 270px; text-align: center; color: var(--text);
  }
  .brand {
    font-weight: 700; font-size: 54px; letter-spacing: 4px;
    color: var(--accent); line-height: 1;
  }
  .name {
    margin-top: 10px;
    font-weight: 700; font-size: 19px; letter-spacing: 2px;
    color: var(--accent); text-transform: uppercase;
  }
  .role { font-size: 13px; font-weight: 500; margin-top: 2px; }
  .divider {
    display: flex; align-items: center; gap: 6px;
    margin: 10px auto 8px; width: 200px;
  }
  .divider::before, .divider::after {
    content: ""; flex: 1; height: 1px; background: var(--muted);
  }
  .icon { width: 16px; height: 16px; }
  .contact { font-size: 13px; line-height: 1.4; font-weight: 500; }
  .rule { width: 200px; height: 1px; background: var(--muted); margin: 8px auto; }
  .address { font-size: 12.5px; font-weight: 500; }
</style>
</head>
<body>
<main class="stage">
  <section class="card card--back" aria-label="Card back">
    <div class="back-mark">NURLO</div>
  </section>

  <section class="card card--front" aria-label="Card front">
    <div class="portrait" role="img" aria-label="Portrait photo of the agent in a dark suit"></div>
    <div class="details">
      <div class="brand">NURLO</div>
      <div class="name">Liam Hartley</div>
      <div class="role">Licenced Real Estate Agent</div>
      <div class="divider">
        <svg class="icon" viewBox="0 0 16 16" aria-hidden="true"><circle cx="8" cy="8" r="8" fill="#e8141c"/><path d="M5.3 4.2l1.3 1.6-.8.9c.5 1.1 1.3 1.9 2.4 2.4l.9-.8 1.6 1.3-.7 1.3C7.6 10.8 5.2 8.4 4 5l1.3-.8z" fill="#fff"/></svg>
        <svg class="icon" viewBox="0 0 16 16" aria-hidden="true"><circle cx="8" cy="8" r="8" fill="#e8141c"/><rect x="4" y="5.2" width="8" height="5.6" fill="#fff"/><path d="M4 5.2l4 3 4-3" fill="none" stroke="#e8141c" stroke-width=".9"/></svg>
        <svg class="icon" viewBox="0 0 16 16" aria-hidden="true"><circle cx="8" cy="8" r="8" fill="#e8141c"/><circle cx="8" cy="8" r="4" fill="none" stroke="#fff" stroke-width="1"/><path d="M4 8h8M8 4c-2 2.4-2 5.6 0 8M8 4c2 2.4 2 5.6 0 8" fill="none" stroke="#fff" stroke-width=".8"/></svg>
      </div>
      <div class="contact">
        <div>0412 583 904</div>
        <div>liam@nurlo.com</div>
        <div>www.nurlo.com</div>
      </div>
      <div class="rule"></div>
      <div class="address">PO Box 3170, Kellmere NSW 2741</div>
    </div>
  </section>
</main>
</body>
</html>
```